a customWebsite for our live Escape room with landing page and then links to the multiple locations

We are looking for a new main landing page that then goes to the location site So puzzlevaultco.com (main landing page)
The site needs to have main company info locations to choose a countdown clock and book now option news articles and video, a link to social media.
a link to the locations
the locations page will go to puzzlevaultcodm.com or puzzlevaultcomke.com for the des moines location and the milwaukee location with more locations opening soon. The location pages need to have a one page theme with book now options and social media links. We are a escape room company please visit puzzlevaultcodm.com to get a idea of what we are looking for. We want to work with someone that can also do updates as we add new rooms etc.. Also must be able to design and upload the site to hostorbitly for us. We would like the countdown timer to display a message at the end (promo code etc) All pages need to link back to the main page and the Des moines Location needs to link to rqtvaultdesk.com. We are looking for a interactive responsive site that shows what we are. The room bios for the MKE location will be upfoaded soon the rooms for des moines are on puzzlevaultcodm.com. please google escape rooms and visit competitor sites to help get more ideas we are open to color changes or logo changes we just shared a video and article on facebook to help http://www.plainsdailyherald.com/story/entertainment/2015/02/19/puzzle-vault-co-des-moines/58812046/

Reason: Not one design has had a landing page with the links to the locations etc....

Reason: Still looking for a main page for puzzle vault co on the main landing page stuff about escape games news stories who should try also a video feed and countdown timmer then a link to des moines and Milwaukee location on the milwaukee page info on the location and the rooms with a book now option. on the des moines location info on the location and rooms with a book now location pages should have links to facebook twitter for that location

Target Market(s)

Customers looking for information about our escape rooms

Industry/Entity Type

It Company

Number of Pages Required

4 page

Requirements
Must have
• main landing page, Des Moines Location Page, Milwaukee Location Page
• booking page
Nice to have
• Be creative look at our page and other pages related to escape rooms to get ideas

```html
<!DOCTYPE html>
<html lang="en">
<head>
<meta charset="utf-8">
<title>Puzzle Vault Co – Why Us?</title>
<link rel="stylesheet" href="https://fonts.googleapis.com/css2?family=Ubuntu:wght@400&family=Ubuntu+Condensed&display=swap">
<style>
  :root {
    --brand-red: #c62127;
    --white: #ffffff;
    --gold: #f7d21e;
    --connector: #f2c23a;
    --title-olive: #a8921f;
    --screen-dark: #3e4247;
    --screen-light: #9ea2a7;
  }
  * { box-sizing: border-box; margin: 0; padding: 0; }
  html, body { width: 1200px; height: 900px; overflow: hidden; background: var(--white); }
  body { position: relative; font-family: "Ubuntu Condensed", "Arial Narrow", sans-serif; }

  .hero-screen {
    position: absolute; left: 214px; top: 0; width: 783px; height: 42px;
    border-radius: 0 0 4px 4px;
    background: radial-gradient(ellipse at 50% 0%, #1c1e21 0%, var(--screen-dark) 30%, var(--screen-light) 75%, #5a5e63 100%);
    border: 2px solid #5b5f64; border-top: none;
    box-shadow: 0 8px 10px -4px rgba(0,0,0,0.35);
  }

  .why-us {
    position: absolute; left: 0; top: 95px; width: 1200px; height: 688px;
    background: var(--brand-red);
  }
  .section-title {
    font-family: "Ubuntu", sans-serif; font-weight: 400;
    font-size: 30px; text-align: center; letter-spacing: 0.5px;
  }
  .why-us .section-title { color: var(--white); position: absolute; top: 34px; width: 100%; }
  .connectors { position: absolute; left: 0; top: 0; }

  .audience-card {
    position: absolute; top: 235px; width: 267px; height: 383px;
    background: var(--white); border-radius: 4px;
    box-shadow: 0 9px 8px -4px rgba(0,0,0,0.35);
    text-align: center; padding: 12px 6px 0;
  }
  .audience-card h3 {
    font-family: "Ubuntu", sans-serif; font-weight: 400;
    font-size: 17.5px; color: var(--title-olive); line-height: 24px;
  }
  .audience-card p {
    margin-top: 20px; font-size: 12.4px; line-height: 14.4px; color: var(--brand-red);
  }
  .card-gamers { left: 54px; }
  .card-gamers p { padding: 0 22px; }
  .card-families { left: 332px; }
  .card-families p { padding: 0 6px; }
  .card-corporate { left: 610px; }
  .card-corporate p { padding: 0 12px; }
  .card-visiting { left: 888px; }

  .rooms-heading {
    position: absolute; top: 816px; width: 100%; color: var(--brand-red);
  }
</style>
</head>
<body>
  <div class="hero-screen" role="img" aria-label="Display screen showing the escape room showcase"></div>

  <section class="why-us">
    <h2 class="section-title">Why Us?</h2>

    <svg class="connectors" width="1200" height="240" viewBox="0 0 1200 240" aria-hidden="true">
      <defs>
        <marker id="arrowhead" markerWidth="6" markerHeight="6" refX="5" refY="3" orient="auto">
          <path d="M0,0 L6,3 L0,6 z" fill="var(--connector)"/>
        </marker>
      </defs>
      <g stroke="var(--connector)" stroke-width="1.2" fill="none">
        <line x1="594" y1="117" x2="478" y2="117" marker-end="url(#arrowhead)"/>
        <line x1="456" y1="117" x2="200" y2="117" marker-end="url(#arrowhead)"/>
        <line x1="614" y1="117" x2="730" y2="117" marker-end="url(#arrowhead)"/>
        <line x1="753" y1="117" x2="1008" y2="117" marker-end="url(#arrowhead)"/>
        <line x1="187" y1="126" x2="187" y2="229" marker-end="url(#arrowhead)"/>
        <line x1="465" y1="126" x2="465" y2="229" marker-end="url(#arrowhead)"/>
        <line x1="743" y1="126" x2="743" y2="229" marker-end="url(#arrowhead)"/>
        <line x1="1021" y1="126" x2="1021" y2="229" marker-end="url(#arrowhead)"/>
      </g>
      <g fill="var(--gold)">
        <circle cx="187" cy="117" r="7.5"/>
        <circle cx="465" cy="117" r="7.5"/>
        <circle cx="604" cy="117" r="7.5"/>
        <circle cx="743" cy="117" r="7.5"/>
        <circle cx="1021" cy="117" r="7.5"/>
      </g>
    </svg>

    <article class="audience-card card-gamers">
      <h3>Gamers &amp; Brainiacs</h3>
      <p>Are people in awe of your gaming skills? Do you always seem to find yourself being the smartest person in the room? Do activities like Sudoku, crossword puzzles, brain-teasers, or trivia games leave you wanting more? Do you crav that rush of adrenaline that goes along with overcoming an intense mental challenge, with only seconds to spare? Yeah….you want to be here.</p>
    </article>

    <article class="audience-card card-families">
      <h3>Families</h3>
      <p>Ever try to have a fun game night with the family,only to find that your living room could get disasterrelief funding from the Disaster Aid Bureau, halfway through a roundof Landlord Lane Does LINE-UP-4 become, Disconnect-your-hands-from-your-brother’s-neck??Does Conquest elicit more violent reactions, from the kids, than Emperor Aldric’s march across Europe?? Puzzle Vault Co DM can help. Instead of pitting family member against family member, you must work together with your loving, caring, beautiful family, to solve the puzzles and escape before time runs out.We’re not doctors, but we’re pretty sure you can skip this week’s family counseling session and come hangout with us! (We’re WAY cheaper than a shrink.)</p>
    </article>

    <article class="audience-card card-corporate">
      <h3>Corporate/Team-building Events</h3>
      <p>Excluding time sleeping, the average American spends 53.4% of their day, at work. Over half of our waking hours are spent with coworkers, doing the things we have to do, not necessarily things we WANT to do, to earn a paycheck. Very few of us have an opportunity to spend time with our coworkers, actually having FUN! How much better would the work day be if you and your fellow work-mates were able to share an experience, which allows you to have a great time, while simultaneously showing your bosses that you are a strong leader, capable of thinking outside of the box, able to multi-task, and can keep a cool head under pressure…all while meeting your 60 minute deadline? Looks like Puzzle Vault Co DM will make you a shoe-in for that promotion. Your future paychecks will thank us, later.</p>
    </article>

    <article class="audience-card card-visiting">
      <h3>Just Visiting</h3>
      <p>You made it….your destination….after the long flight, held hostage by a screaming 3 year old with lungs like Marla Vance, or the car ride that took you far away from all of those and mountainous vistas and clear blue waters throughout this great country of ours….you just can’t believe you’re about to see the most perfectly flat cornfields you could ever imagine. My God….it’s beautiful. But you didn’t come all the way to Des Moines, just for that…you want more. Is this heaven? No, it’s Puzzle Vault Co DM. DesMoines is known for having some of the best places to eat, in the nation, and while other destinations across the country are content to give you a taste of what is an escape room, we are serving up Thanksgiving dinner! If you want an experience that will change your definition of the word “WOW!”…let us show you how it’s done.</p>
    </article>
  </section>

  <h2 class="section-title rooms-heading">Rooms</h2>
</body>
</html>
```